Waste and recycling company seeks artwork design and branding for plastic ruler.

We require a very professional design for our marketing product 'Ruler'.
It will be on a white plastic ruler 315mm long and 39mm high.
0 – 30 on the top (in mm).
0 – 12 on the bottom (in inches).
Numbering in black (to be included as an example only) as it is already printed on the plastic stock.
3 colours. Red, Black, Harbor crewman blue (colour is Pantone 3155C)
Total workable text area –
Length 312mm
Height 24mm
We would need the artwork in a vector format, either .pdf or .eps

Version 1 - Try and fit all the following info onto it.

Dot points -
• Commercial waste and recycling
• Bulk clean up bins
• Document shredding
• Liquid waste

08 8394 7261
info@kestrelbins.com.au
www.kestrelbins.com.au

SA Family owned and operated.

Kestrel logo

With service YOU can measure
Backed by our 5 Star customer service guarantee

I would like dot points on the left side of ruler. Kestrel logo in the middle of the ruler or on the far right hand side.
If Kestrel logo is in the middle, then ‘with service you can measure backed by our customer service guarantee.' to the right

Version 2. If all this does not fit -
Try having no dot points and have on the left hand side
'SA Family Owned and Operated'
Underneath ‘Phone 08 8394 7261
Underneath website and email
Kestrel logo

Target Market(s)

business clients

Industry/Entity Type

Recycling

Requirements
Must have
• phone number, email, logo,

```html
<!DOCTYPE html>
<html lang="en">
<head>
<meta charset="utf-8">
<title>Kestrel Waste &amp; Recycling – Ruler Artwork</title>
<link rel="stylesheet" href="https://fonts.googleapis.com/css2?family=Archivo+Black&family=Arimo:ital,wght@0,400;0,700;1,400&display=swap">
<style>
  :root {
    --page-bg: #ebebeb;
    --ruler-white: #ffffff;
    --tick-grey: #9a9a9a;
    --harbor-blue: #0b5d6e;
    --harbor-light-1: #5f98a5;
    --harbor-light-2: #9dc0c8;
    --harbor-light-3: #cfe1e5;
    --brand-red: #d7262b;
    --brand-red-dark: #7d1014;
    --ink: #111111;
    --white: #ffffff;
  }
  * { box-sizing: border-box; margin: 0; padding: 0; }
  html, body {
    width: 1200px;
    height: 818px;
    overflow: hidden;
    background: var(--page-bg);
    font-family: "Arimo", Arial, sans-serif;
  }
  .canvas { position: relative; width: 1200px; height: 818px; }

  .ruler {
    position: absolute;
    left: 55px;
    width: 1075px;
    height: 133px;
    background-color: var(--ruler-white);
    border-bottom: 1px solid #c9c9c9;
    box-shadow: 2px 2px 3px rgba(0, 0, 0, 0.35);
  }
  .ruler--v1 { top: 196px; }
  .ruler--v2 { top: 458px; }

  .ruler__scale {
    position: absolute;
    left: 24px;
    right: 8px;
    height: 14px;
  }
  .ruler__scale--mm {
    top: 0;
    background:
      linear-gradient(var(--tick-grey), var(--tick-grey)) top left / 1px 12px repeat-x,
      repeating-linear-gradient(90deg, var(--tick-grey) 0 1px, transparent 1px 17.05px) top left / 100% 9px no-repeat,
      repeating-linear-gradient(90deg, var(--tick-grey) 0 1px, transparent 1px 3.41px) top left / 100% 5px no-repeat;
    background-size: 34.1px 12px, 100% 9px, 100% 5px;
  }
  .ruler__scale--inch {
    bottom: 0;
    background:
      repeating-linear-gradient(90deg, var(--tick-grey) 0 1px, transparent 1px 86.6px) bottom left / 100% 13px no-repeat,
      repeating-linear-gradient(90deg, var(--tick-grey) 0 1px, transparent 1px 43.3px) bottom left / 100% 9px no-repeat,
      repeating-linear-gradient(90deg, var(--tick-grey) 0 1px, transparent 1px 10.83px) bottom left / 100% 5px no-repeat;
  }

  .banner {
    position: absolute;
    left: 4px;
    top: 26px;
    width: 600px;
    height: 81px;
  }
  .banner__shape { position: absolute; inset: 0; }
  .banner__headline {
    position: absolute;
    left: 28px;
    top: -3px;
    font-family: "Archivo Black", "Arial Black", sans-serif;
    font-size: 28.5px;
    letter-spacing: 0.2px;
    color: var(--brand-red);
    -webkit-text-stroke: 0.8px var(--brand-red-dark);
    text-shadow: 2px 2px 2px rgba(0, 0, 0, 0.55);
    white-space: nowrap;
  }
  .banner__promise {
    position: absolute;
    left: 28px;
    top: 33px;
    font-size: 22px;
    font-weight: 700;
    letter-spacing: 0.3px;
    color: var(--white);
    white-space: nowrap;
  }
  .banner__contact {
    position: absolute;
    left: 28px;
    top: 60px;
    font-size: 13.5px;
    color: var(--white);
    white-space: nowrap;
  }
  .banner__contact .sep { margin: 0 6px; font-size: 9px; vertical-align: 2px; }

  .services { list-style: none; position: absolute; top: 0; left: 0; }
  .services li {
    position: absolute;
    font-size: 13px;
    color: var(--ink);
    white-space: nowrap;
    line-height: 16px;
  }
  .services li::before { content: "\25AA"; margin-right: 9px; font-size: 10px; }
  .services li:nth-child(1) { left: 630px; top: 28px; }
  .services li:nth-child(2) { left: 622px; top: 48px; }
  .services li:nth-child(3) { left: 614px; top: 67px; }
  .services li:nth-child(4) { left: 606px; top: 87px; }
  .ruler--v2 .services li { font-weight: 700; }

  .brand {
    position: absolute;
    left: 860px;
    top: 38px;
    width: 175px;
    display: flex;
    align-items: center;
    gap: 10px;
  }
  .brand__name {
    font-size: 26px;
    font-weight: 700;
    color: var(--ink);
    letter-spacing: 0.5px;
  }
  .brand__dot {
    width: 34px;
    height: 34px;
    border-radius: 50%;
    background: var(--harbor-blue);
  }
  .brand__tagline {
    position: absolute;
    left: 860px;
    top: 86px;
    font-size: 12px;
    font-style: italic;
    color: var(--harbor-blue);
    white-space: nowrap;
  }
</style>
</head>
<body>
<main class="canvas">

  <section class="ruler ruler--v1">
    <div class="ruler__scale ruler__scale--mm"></div>
    <div class="ruler__scale ruler__scale--inch"></div>

    <div class="banner">
      <svg class="banner__shape" viewBox="0 0 600 81" width="600" height="81">
        <polygon points="0,0 560,0 536,81 0,81" fill="var(--harbor-blue)"/>
        <polygon points="560,0 571,0 547,81 536,81" fill="var(--harbor-light-1)"/>
        <polygon points="571,0 582,0 558,81 547,81" fill="var(--harbor-light-2)"/>
        <polygon points="582,0 594,0 570,81 558,81" fill="var(--harbor-light-3)"/>
        <polygon points="0,0 560,0 556,14 0,14" fill="#ffffff" opacity="0.12"/>
      </svg>
      <p class="banner__headline">With service YOU can measure</p>
      <p class="banner__promise">5 star customer service guarantee</p>
      <p class="banner__contact">08 8394 7261<span class="sep">&#9632;</span>info@kestrelbins.com.au<span class="sep">&#9632;</span>www.kestrelbins.com.au</p>
    </div>

    <ul class="services">
      <li>Commercial waste and recycling</li>
      <li>Document shredding</li>
      <li>Bulk clean up bins</li>
      <li>Liquid waste</li>
    </ul>

    <div class="brand"><span class="brand__name">KESTREL</span><span class="brand__dot"></span></div>
    <p class="brand__tagline">SA family owned and operated</p>
  </section>

  <section class="ruler ruler--v2">
    <div class="ruler__scale ruler__scale--mm"></div>
    <div class="ruler__scale ruler__scale--inch"></div>

    <div class="banner">
      <svg class="banner__shape" viewBox="0 0 600 81" width="600" height="81">
        <polygon points="0,0 560,0 536,81 0,81" fill="var(--harbor-blue)"/>
        <polygon points="560,0 571,0 547,81 536,81" fill="var(--harbor-light-1)"/>
        <polygon points="571,0 582,0 558,81 547,81" fill="var(--harbor-light-2)"/>
        <polygon points="582,0 594,0 570,81 558,81" fill="var(--harbor-light-3)"/>
        <polygon points="0,0 560,0 556,14 0,14" fill="#ffffff" opacity="0.12"/>
      </svg>
      <p class="banner__headline">With service YOU can measure</p>
      <p class="banner__promise">YOUR 5 star customer service guarantee</p>
      <p class="banner__contact">08 8394 7261<span class="sep">&#9632;</span>info@kestrelbins.com.au<span class="sep">&#9632;</span>www.kestrelbins.com.au</p>
    </div>

    <ul class="services">
      <li>Commercial waste and recycling</li>
      <li>Document shredding</li>
      <li>Bulk clean up bins</li>
      <li>Liquid waste</li>
    </ul>

    <div class="brand"><span class="brand__name">KESTREL</span><span class="brand__dot"></span></div>
    <p class="brand__tagline">SA family owned and operated</p>
  </section>

</main>
</body>
</html>
```